Design business cards for Ironvale Barbers (Opening March so won't need finalised till January2018

Ironvale Barbers is the new age barbers and skincare for all men. Creating tailor made haircuts & customised skincare solutions for the perfect healthy manly look. The Barbers will have a industrial, rustic, worldly feel about it. Rustic red brick wall with old wine barrels as the work stations with the old fashion barber chairs. Concrete floor and a bit corrugated iron around.
Target Market(s)
Professional males who like a great haircut, wet shave and may consider a facial if in the right environment. Total pampering experience in a boys environment.
Industry/Entity Type
Barber
Contact Information for Business Card
Front- Logo - address is 42 Kowhai Rd Taupo
Ph - (07) 548 9163
www.ironvalebarbers.com
email - hello@ironvale.co.nz
Back of card
Mens Haircare - Wet Shaving - Facials - Skin Prescriptions
We are doing a loyalty program - 6 squares numbered then 7th free
Colors
Designer to choose colors to be used in the design.
Requirements
Must have
- Clean simple easy to read.
Nice to have
- Our current colours are white font on black background but thinking we need to introduce another colour. Maybe white logo on a copper, bronze or rusty background. Or even a rustic red brick wall with white writing. Want it clean simple to read. Maybe a burgundy?
Should not have
- no images like heads, scissors, razors please

```html
<!DOCTYPE html>
<html lang="en">
<head>
<meta charset="utf-8">
<title>Ironvale Barbers – Business Cards</title>
<link href="https://fonts.googleapis.com/css2?family=Barlow:wght@400;500;600&display=swap" rel="stylesheet">
<style>
  :root {
    --page-bg: #e9e8e6;
    --card-dark: #1e1e20;
    --card-mid: #2c2c2f;
    --barrel-dark: #2f2419;
    --barrel-mid: #5a4532;
    --ink: #ffffff;
    --ink-soft: #e6e6e6;
  }
  * { box-sizing: border-box; margin: 0; padding: 0; }
  html, body { width: 1200px; height: 800px; overflow: hidden; }
  body {
    background: var(--page-bg);
    font-family: "Barlow", Arial, sans-serif;
    color: var(--ink);
    position: relative;
  }
  .card {
    position: absolute;
    top: 110px;
    width: 330px;
    height: 580px;
    overflow: hidden;
    text-align: center;
  }
  .card--back { left: 235px; }
  .card--front { left: 635px; }
  .card__wall {
    position: absolute; inset: 0;
    background: linear-gradient(180deg, var(--card-dark) 0%, var(--card-mid) 55%, var(--card-dark) 100%);
  }
  .card__barrel {
    position: absolute; left: 0; right: 0; bottom: 0; height: 92px;
    background: linear-gradient(180deg, var(--barrel-mid) 0%, var(--barrel-dark) 100%);
  }
  .card__content { position: absolute; inset: 0; }
  .brand {
    position: absolute; left: 0; right: 0; top: 40px;
    font-weight: 600; color: var(--ink);
    line-height: 1;
  }
  .brand__name { display: block; font-size: 40px; letter-spacing: 1px; text-transform: uppercase; }
  .brand__sub { display: block; font-size: 17px; letter-spacing: 5px; text-transform: uppercase; margin-top: 6px; }
  .services {
    position: absolute; left: 0; right: 0; top: 148px;
    list-style: none; font-weight: 500; font-size: 30px; line-height: 41px;
  }
  .field-label {
    position: absolute; left: 0; right: 0;
    font-weight: 500; font-size: 21px;
  }
  .field-line {
    position: absolute; left: 20px; right: 20px; height: 3px; background: var(--ink);
  }
  .person { position: absolute; left: 0; right: 0; top: 218px; }
  .person__name { font-weight: 600; font-size: 26px; }
  .person__role { font-size: 20px; color: var(--ink-soft); margin-top: 2px; }
  .contact { position: absolute; left: 0; right: 0; top: 370px; line-height: 24px; }
  .contact__phone { font-weight: 600; font-size: 26px; margin-bottom: 3px; }
  .contact__line { font-size: 19px; color: var(--ink-soft); }
  .web {
    position: absolute; left: 0; right: 0; bottom: 20px;
    font-weight: 500; font-size: 22px;
  }
</style>
</head>
<body>

<section class="card card--back">
  <div class="card__wall" role="img" aria-label="Dark painted brick wall texture"></div>
  <div class="card__barrel" role="img" aria-label="Weathered oak wine barrel"></div>
  <div class="card__content">
    <div class="brand">
      <span class="brand__name">Ironvale</span>
      <span class="brand__sub">Barbers</span>
    </div>
    <ul class="services">
      <li>Mens Haircare</li>
      <li>Wet Shaving</li>
      <li>Facials</li>
      <li>Skin Prescriptions</li>
    </ul>
    <div class="field-label" style="top:330px;">Date</div>
    <div class="field-line" style="top:385px;"></div>
    <div class="field-label" style="top:412px;">Time</div>
    <div class="field-line" style="top:468px;"></div>
    <div class="web">www.ironvalebarbers.com</div>
  </div>
</section>

<section class="card card--front">
  <div class="card__wall" role="img" aria-label="Dark painted brick wall texture"></div>
  <div class="card__barrel" role="img" aria-label="Weathered oak wine barrel"></div>
  <div class="card__content">
    <div class="brand">
      <span class="brand__name">Ironvale</span>
      <span class="brand__sub">Barbers</span>
    </div>
    <div class="person">
      <div class="person__name">FullName Surname</div>
      <div class="person__role">Position</div>
    </div>
    <div class="contact">
      <div class="contact__phone">000-000-0000</div>
      <div class="contact__line">42 Kowhai Rd Taupo</div>
      <div class="contact__line">hello@ironvale.co.nz</div>
    </div>
    <div class="web">www.ironvalebarbers.com</div>
  </div>
</section>

</body>
</html>
```